I'm looking for a fresh new design for my business Martin Coldwell Creative.
I am a photographer and videographer.
The card must be easy to print, eye catching and easy to read. It must reflect the fact that I work in a creative area, but not so edgy as to scare away my corporate clients.
Sub text should read Photography, Video, Design
There also needs to be room for phone number and email.

```html
<!DOCTYPE html>
<html lang="en">
<head>
<meta charset="utf-8">
<title>Martin Coldwell Creative — Business Card</title>
<link rel="stylesheet" href="https://fonts.googleapis.com/css2?family=Open+Sans:wght@400;600;700&display=swap">
<style>
  :root {
    --backdrop: #e6e6e6;
    --card: #1d1d1d;
    --ink: #ffffff;
    --ink-soft: #e4e4e4;
    --mark: #a8a8a8;
    --band-end: #4a4a4a;
    --band-edge: #6e6e6e;
    --icon-bg: #8d8d8d;
  }
  html, body {
    margin: 0;
    width: 1200px;
    height: 900px;
    overflow: hidden;
    background: var(--backdrop);
    font-family: "Open Sans", sans-serif;
  }
  .business-card {
    position: absolute;
    left: 150px;
    top: 193px;
    width: 900px;
    height: 514px;
    background: var(--card);
    border-radius: 4px;
    overflow: hidden;
  }
  .brand-dot {
    position: absolute;
    left: 70px;
    top: 92px;
    width: 220px;
    height: 220px;
    border-radius: 50%;
    background: var(--mark);
  }
  .name-band {
    position: absolute;
    left: 300px;
    top: 96px;
    width: 440px;
    height: 58px;
    box-sizing: border-box;
    padding-left: 26px;
    display: flex;
    align-items: center;
    border-radius: 0 29px 29px 0;
    background: linear-gradient(90deg, rgba(74,74,74,0) 0%, var(--band-end) 70%);
    border-right: 4px solid var(--band-edge);
  }
  .brand-name {
    margin: 0;
    font-size: 31px;
    font-weight: 700;
    color: var(--ink);
    white-space: nowrap;
  }
  .brand-services {
    position: absolute;
    left: 334px;
    top: 170px;
    margin: 0;
    font-size: 21px;
    font-weight: 600;
    color: var(--ink-soft);
  }
  .contact-list {
    position: absolute;
    right: 56px;
    top: 318px;
    margin: 0;
    padding: 0;
    list-style: none;
    color: var(--ink);
    font-size: 23px;
  }
  .contact-item {
    display: flex;
    align-items: center;
    gap: 10px;
    margin-bottom: 14px;
    white-space: nowrap;
  }
  .contact-icon {
    width: 24px;
    height: 24px;
    flex: none;
  }
</style>
</head>
<body>
  <main class="business-card">
    <span class="brand-dot"></span>
    <div class="name-band">
      <h1 class="brand-name">Martin Coldwell Creative</h1>
    </div>
    <p class="brand-services">Photography, Video, Design</p>

    <ul class="contact-list">
      <li class="contact-item">
        <svg class="contact-icon" viewBox="0 0 24 24" aria-hidden="true">
          <rect x="1" y="1" width="22" height="22" rx="4" fill="var(--icon-bg)"/>
          <rect x="8" y="4" width="8" height="16" rx="1.5" fill="none" stroke="#fff" stroke-width="1.6"/>
          <line x1="10.5" y1="17.5" x2="13.5" y2="17.5" stroke="#fff" stroke-width="1.4"/>
        </svg>
        <span>0000050700</span>
      </li>
      <li class="contact-item">
        <svg class="contact-icon" viewBox="0 0 24 24" aria-hidden="true">
          <rect x="1" y="1" width="22" height="22" rx="4" fill="var(--icon-bg)"/>
          <rect x="4" y="7" width="16" height="11" fill="#fff"/>
          <polyline points="4,7 12,13 20,7" fill="none" stroke="var(--icon-bg)" stroke-width="1.4"/>
        </svg>
        <span>hello@coldwellcrtv.com</span>
      </li>
    </ul>
  </main>
</body>
</html>
```